Indoor Gun Range Web Design Project

Create a professional bold indoor gun range website. Logo colors are white, red, and black. This is a very professional gun range. Please use high quality stock images if possible. Stay away from a lot of militia type photos. Use your best judgement on what to put as a main image and headline.

Here are some websites that I like for design.

http://www.pinebrookarsenal.example/
http://www.layoutbazaar.example/website-templates/51947.html
http://www.marigoldworks.example/

Target Market(s)

Men ages 25-65

Industry/Entity Type

Gun

Requirements
Must have
• Bold lettering, logo attached, exciting photos.
Should not have
• A lot of militia photos.

```html
<!DOCTYPE html>
<html lang="en">
<head>
<meta charset="utf-8">
<title>True Mark Indoor Range</title>
<link href="https://fonts.googleapis.com/css2?family=Archivo+Narrow:wght@400;700&family=Michroma&family=Roboto+Condensed:wght@400;700&display=swap" rel="stylesheet">
<style>
  :root{
    --red:#c8101a;
    --red-dark:#8e0a10;
    --black:#0c0c0c;
    --frame-light:#d2d2d2;
    --frame-dark:#9a9a9a;
    --white:#ffffff;
    --ink:#222222;
  }
  *{box-sizing:border-box;margin:0;padding:0}
  html,body{width:1200px;height:900px;overflow:hidden}
  body{position:relative;background:var(--black);font-family:"Archivo Narrow",Arial,sans-serif;color:var(--ink)}
  a{text-decoration:none}
  .site-header{position:absolute;left:0;top:0;width:1200px;height:216px;
    background:linear-gradient(180deg,#ffffff 0%,#f4f4f4 55%,#dcdcdc 100%)}
  .stage{position:absolute;left:0;top:216px;width:1200px;height:618px;
    background:radial-gradient(ellipse at 50% 30%,#2a2a2a 0%,#111 55%,#050505 100%)}
  .brand{position:absolute;left:50px;top:62px;display:flex;align-items:center;gap:16px}
  .brand-name{font-weight:700;font-size:40px;color:var(--red);letter-spacing:1px;line-height:1}
  .brand-mark{width:58px;height:58px;border-radius:50%;background:var(--black)}
  .main-nav{position:absolute;left:0;top:156px;width:1200px;height:130px}
  .nav-item{position:absolute;width:140px;margin-left:-70px;text-align:center}
  .nav-label{font-size:20px;color:var(--ink);text-transform:uppercase;display:block;height:28px}
  .nav-badge{display:block;margin:4px auto 0;width:58px;height:58px;border-radius:50%;
    background:radial-gradient(circle,#fff 0%,#e0e0e0 70%,#bdbdbd 100%);position:relative}
  .nav-badge span{position:absolute;left:8px;top:8px;width:42px;height:42px;border-radius:50%;
    background:radial-gradient(circle at 40% 35%,#e8323a 0%,var(--red) 45%,var(--red-dark) 100%);
    color:#fff;font-weight:700;font-size:22px;line-height:42px}
  .nav-pin{display:block;margin:0 auto;width:2px;height:24px;background:#9a9a9a;position:relative}
  .nav-pin::after{content:"";position:absolute;left:-4px;bottom:-6px;width:10px;height:10px;border-radius:50%;background:#d6d6d6}
  .showcase{position:absolute;left:146px;top:294px;width:900px;height:330px;
    background:linear-gradient(180deg,var(--frame-light),var(--frame-dark));border-radius:6px}
  .slider{position:absolute;left:12px;top:12px;width:636px;height:306px;background:var(--black);border-radius:3px}
  .hero-photo{position:absolute;left:19px;top:7px;width:394px;height:255px;
    background:linear-gradient(135deg,#6d3a23 0%,#a86a3f 40%,#3b3b3b 75%,#1a1a1a 100%)}
  .side-photo{position:absolute;left:435px;top:7px;width:175px;height:255px;
    background:linear-gradient(160deg,#7a6a58 0%,#4a4035 50%,#1e1e1e 100%)}
  .pager{position:absolute;left:26px;top:273px;display:flex;background:var(--red-dark);padding:2px 4px}
  .pager span{width:21px;height:20px;font-size:13px;color:#fff;text-align:center;line-height:20px}
  .pager .is-active{background:#555}
  .quick-links{position:absolute;left:658px;top:12px;width:233px}
  .quick-link{display:block;height:96px;margin-bottom:8px;border:2px solid #888;border-radius:4px;background:var(--black);
    font-family:"Michroma",Arial,sans-serif;color:#fff;font-size:18px;letter-spacing:2px;padding:14px 10px;line-height:1.3;text-transform:uppercase}
  .scroller{position:absolute;left:1108px;top:291px;width:46px;height:512px}
  .scroller-track{position:absolute;left:22px;top:20px;width:2px;height:470px;
    background:repeating-linear-gradient(180deg,#888 0 6px,transparent 6px 12px)}
  .scroller-cap{position:absolute;left:6px;width:34px;height:34px;border-radius:50%;
    background:radial-gradient(circle at 40% 35%,#ff4a50 0%,var(--red) 50%,var(--red-dark) 100%);border:3px solid #444}
  .scroller-thumb{position:absolute;left:12px;top:212px;width:22px;height:101px;border-radius:11px;
    background:linear-gradient(90deg,var(--red-dark),#e0262e,var(--red-dark));border:2px solid #444}
  .cards{position:absolute;left:0;top:656px}
  .card{position:absolute;top:0;width:278px;height:141px;background:var(--white);border-radius:4px}
  .card-title{position:absolute;left:14px;top:6px;width:250px;height:24px;border-radius:4px;
    background:linear-gradient(180deg,#3a3a3a,#0c0c0c);color:#fff;text-align:center;
    font-family:"Roboto Condensed",Arial,sans-serif;font-weight:700;font-size:17px;line-height:24px;text-transform:uppercase}
  .card-thumb{position:absolute;left:18px;top:44px;width:80px;height:58px;background:linear-gradient(135deg,#3a3a3a,#111)}
  .card-text{position:absolute;left:112px;top:44px;width:156px;font-family:"Roboto Condensed",Arial,sans-serif;font-size:10px;line-height:1.5;text-transform:uppercase;color:var(--ink)}
  .card-text.is-wide{left:36px;width:230px}
  .read-more{position:absolute;right:12px;bottom:8px;width:114px;height:24px;border-radius:3px;
    background:linear-gradient(180deg,#e0262e,var(--red-dark));color:#fff;text-align:center;
    font-family:"Roboto Condensed",Arial,sans-serif;font-size:13px;line-height:24px;text-transform:uppercase}
  .site-footer{position:absolute;left:0;top:834px;width:1200px;height:66px;
    background:linear-gradient(180deg,#e0262e 0%,var(--red) 40%,var(--red-dark) 100%)}
</style>
</head>
<body>
  <header class="site-header">
    <div class="brand">
      <span class="brand-name">TRUE MARK INDOOR RANGE</span>
      <span class="brand-mark"></span>
    </div>
  </header>

  <main class="stage"></main>

  <nav class="main-nav">
    <div class="nav-item" style="left:188px"><span class="nav-label">Home</span><span class="nav-badge"><span>1</span></span><span class="nav-pin"></span></div>
    <div class="nav-item" style="left:351px"><span class="nav-label">Range Fees</span><span class="nav-badge"><span>2</span></span><span class="nav-pin"></span></div>
    <div class="nav-item" style="left:516px"><span class="nav-label">Range Rules</span><span class="nav-badge"><span>3</span></span><span class="nav-pin"></span></div>
    <div class="nav-item" style="left:688px"><span class="nav-label">Range News</span><span class="nav-badge"><span>4</span></span><span class="nav-pin"></span></div>
    <div class="nav-item" style="left:848px"><span class="nav-label">Membership</span><span class="nav-badge"><span>5</span></span><span class="nav-pin"></span></div>
    <div class="nav-item" style="left:1005px"><span class="nav-label">Contact Us</span><span class="nav-badge"><span>6</span></span><span class="nav-pin"></span></div>
  </nav>

  <section class="showcase">
    <div class="slider">
      <div class="hero-photo" role="img" aria-label="Shooters with ear protection practising at an outdoor firing line"></div>
      <div class="side-photo" role="img" aria-label="Instructor showing a pistol to a student at the range"></div>
      <div class="pager">
        <span>1</span><span class="is-active">2</span><span>3</span><span>4</span><span>5</span><span>6</span>
      </div>
    </div>
    <div class="quick-links">
      <a class="quick-link">Locations</a>
      <a class="quick-link">Sales and Transfers</a>
      <a class="quick-link">Join Now</a>
    </div>
  </section>

  <aside class="scroller">
    <div class="scroller-track"></div>
    <div class="scroller-cap" style="top:3px"></div>
    <div class="scroller-thumb"></div>
    <div class="scroller-cap" style="top:472px"></div>
  </aside>

  <section class="cards">
    <article class="card" style="left:148px">
      <h2 class="card-title">Featured Specials</h2>
      <div class="card-thumb" role="img" aria-label="Black semi-automatic pistol"></div>
      <p class="card-text">Corvane Tactical C90 Pistol, Series 3</p>
      <a class="read-more">Read More</a>
    </article>
    <article class="card" style="left:456px">
      <h2 class="card-title">Upcoming Events</h2>
      <p class="card-text is-wide">Tuesday Night Pistol League<br>January 30, 2012</p>
      <a class="read-more">Read More</a>
    </article>
    <article class="card" style="left:767px">
      <h2 class="card-title">Recent Reviews</h2>
      <div class="card-thumb" role="img" aria-label="Two-tone handgun with wooden grip"></div>
      <p class="card-text">Brightwell B4 Sentry</p>
      <a class="read-more">Read More</a>
    </article>
  </section>

  <footer class="site-footer"></footer>
</body>
</html>
```